Moderne CI für einen Immobilienmakler [www.brekow-immobilien.de]
Zielgruppe
Kunden für hochwertige Immobilien, also gemischtes eher anspruchvolles Klientel.
Hallo,
ich betreibe ein junges Immobilienunternehmen im 4. Geschäftsjahr. Wir vermarkten ausschließlich hochwertige Immobilien. Meine derzeitiges Logo habe ich damals selbst entworfen und es harmoniert gut mit meiner Website [www.brekow-immobilien.de] leider habe ich für Printmedien nie eine CI hinbekommen die mir richtig gefällt und die im Gesamt- und Farbkonzept zu meinem Onlineauftritt passt.
Ich wünsche mir nun von einem professionellen Designer eine modern- edle CI mit Entwürfen für Briefpapier, Umschläge C4 und DL, A4 Exposé-Mappe sowie die Rohlinge für eine Dreiseiter Image-Broschüre, für ein Objekt Expose sowie für eine Print-Annonce.
Eine spätere Zusammenarbeit für weitere Medien ist erwünscht.

```html
<!DOCTYPE html>
<html lang="de">
<head>
<meta charset="utf-8">
<title>Brekow Immobilien – Objekt-Exposé</title>
<link rel="stylesheet" href="https://fonts.googleapis.com/css2?family=Ubuntu:wght@400;500;700&display=swap">
<style>
:root{
  --bg:#4a4a4a;
  --paper:#ffffff;
  --brand-red:#b01e33;
  --brand-red-mid:#c0233b;
  --brand-maroon:#7c1226;
  --accent-head:#b8342a;
  --text:#6b6b6b;
  --logo-grey:#6f6f6f;
  --cell-label:#d6d6d6;
  --cell-value:#ececec;
  --cell-label-alt:#e4e4e4;
  --cell-value-alt:#f5f5f5;
  --footer-yellow:#f6d66a;
  --white:#ffffff;
}
*{margin:0;padding:0;box-sizing:border-box}
html,body{width:871px;height:1200px;overflow:hidden;background:var(--bg)}
body{font-family:"Ubuntu",sans-serif;color:var(--text)}
.sheet{position:absolute;left:25px;top:15px;width:821px;height:1170px;background:var(--paper)}
.logo{position:absolute;left:36px;top:58px;font-size:29px;font-weight:400;color:var(--logo-grey);letter-spacing:.3px}
.hero{position:absolute;left:0;top:111px;width:821px;height:290px;
  background:linear-gradient(100deg,#dfe3e6 0%,#b9c2c9 30%,#7d8f78 55%,#4f7a3a 75%,#3d6a2c 100%)}
.hero-tag{position:absolute;right:15px;top:117px;width:340px;height:38px;background:var(--brand-red);
  color:var(--white);font-size:21px;font-weight:500;display:flex;align-items:center;justify-content:center}
.intro,.contact{position:absolute;left:57px;width:468px}
.intro{top:450px}
.contact{top:786px}
h2{font-size:17px;font-weight:400;color:var(--accent-head);margin-bottom:12px}
p{font-size:14.5px;line-height:19.5px;text-align:justify;letter-spacing:.3px}
.facts{position:absolute;left:545px;top:450px;width:258px}
.facts h3{font-size:17px;font-weight:500;color:#555;text-align:right;margin-bottom:10px}
.facts table{width:100%;border-collapse:separate;border-spacing:0 4px}
.facts td{height:31px;font-size:14px;color:#555;padding:0 8px}
.facts td.label{background:var(--cell-label);text-align:right;width:145px}
.facts td.value{background:var(--cell-value)}
.facts tr:nth-child(even) td.label{background:var(--cell-label-alt)}
.facts tr:nth-child(even) td.value{background:var(--cell-value-alt)}
.interior{position:absolute;left:545px;top:780px;width:258px;height:172px;
  background:linear-gradient(180deg,#f1f1ef 0%,#e2e4e2 55%,#9a6a45 70%,#7e5233 100%)}
.footer{position:absolute;left:0;top:1054px;width:821px;height:86px;display:flex}
.footer .col{padding:12px 14px;font-size:13px;line-height:17px;font-weight:500}
.footer .company{width:290px;background:var(--brand-red)}
.footer .reach{width:290px;background:var(--brand-red-mid)}
.footer .online{flex:1;background:var(--brand-maroon);text-align:right;color:var(--white)}
.footer strong{color:var(--white);font-weight:700}
.footer .line{color:var(--footer-yellow)}
</style>
</head>
<body>
<div class="sheet">
  <div class="logo">brekow-immobilien.de</div>
  <div class="hero" role="img" aria-label="Foto: modernes weißes Mehrfamilienhaus mit Balkonen vor grüner Hügellandschaft"></div>
  <div class="hero-tag">Idyllisch modern Wohnen</div>

  <section class="intro">
    <h2>Ihre zukünftige Eigentumswohnung</h2>
    <p>Lorem ipsum dolor sit amet, consectetur adipiscing elit. Sed quam eros, dapibus et dictum quis, tincidunt et nibh. In hac habitasse platea dictumst. Maecenas euismod commodo blandit. Suspendisse potenti. Curabitur vestibulum, urna eu luctus sagittis, metus erat auctor arcu, vel posuere erat eros eu leo. Nulla facilisi. Nam ornare sagittis enim, venenatis cursus magna suscipit et. Vivamus gravida convallis urna, et convallis nulla hendrerit id. Morbi nibh magna, dignissim at ullamcorper ac, vehicula facilisis lorem. Pellentesque leo lorem, imperdiet et semper at, rutrum eu tellus.</p>
  </section>

  <section class="contact">
    <h2>Ihr Ansprechpartner</h2>
    <p>Lorem ipsum dolor sit amet, consectetur adipiscing elit. Sed quam eros, dapibus et dictum quis, tincidunt et nibh. In hac habitasse platea dictumst. Maecenas euismod commodo blandit. Suspendisse potenti. Curabitur vestibulum, urna eu luctus sagittis, metus erat auctor arcu, vel posuere erat eros eu leo. Nulla facilisi.</p>
  </section>

  <aside class="facts">
    <h3>Objektbezogene Daten</h3>
    <table>
      <tr><td class="label">Kaufpreis:</td><td class="value">175.000,00 €</td></tr>
      <tr><td class="label">Hausgeld:</td><td class="value">210,00 €</td></tr>
      <tr><td class="label">Zimmer:</td><td class="value">5</td></tr>
      <tr><td class="label">Badezimmer:</td><td class="value">1</td></tr>
      <tr><td class="label">Schlafzimmer:</td><td class="value">2</td></tr>
      <tr><td class="label">Wohnfläche:</td><td class="value">150 qm</td></tr>
      <tr><td class="label">Baujahr:</td><td class="value">2008</td></tr>
      <tr><td class="label">Verfügbar ab:</td><td class="value">sofort</td></tr>
    </table>
  </aside>
  <div class="interior" role="img" aria-label="Foto: heller leerer Wohnraum mit Parkettboden und großen Fenstern"></div>

  <footer class="footer">
    <div class="col company">
      <strong>Brekow Immobilien</strong><br>
      <span class="line">Inhaber: Matthias Brekow</span><br>
      <span class="line">Musterweg 1</span><br>
      <span class="line">12345 Musterstadt</span>
    </div>
    <div class="col reach">
      <strong>Kontaktmöglichkeiten</strong><br>
      <span class="line">Telefon: 01234 - 000 001</span><br>
      <span class="line">Telefax: 01234 - 000 002</span><br>
      <span class="line">Mobil: 0100 - 000 0000</span>
    </div>
    <div class="col online">
      info@brekow-immobilien.de<br>
      www.brekow-immobilien.de
    </div>
  </footer>
</div>
</body>
</html>
```